Velmora Care! Create an exciting flyer for our hemodialysis clinic

Create an engaging Flyer that shows our offering and that will drive patients to our hemodialysis clinic. www.velmoracare.example

Target Market(s)

Mass public

Industry/Entity Type

Healthcare

Requirements
Must have
• 1 Our logo. 2. Should include that we accept all insurances 3. Our tag line “Transforming Lives, One Dialysis Session at a Time.”

```html
<!DOCTYPE html>
<html lang="en">
<head>
<meta charset="utf-8">
<title>Velmora Care – In-Center Hemodialysis Clinic Flyer</title>
<link href="https://fonts.googleapis.com/css2?family=Montserrat:ital,wght@0,400;0,500;0,700;0,800;1,600&display=swap" rel="stylesheet">
<style>
  :root {
    --backdrop: #2e5a6b;
    --paper: #ffffff;
    --brand-blue: #1f7bbf;
    --band-blue: #2a81b5;
    --band-green: #56a447;
    --phone-blue: #1a7bc4;
    --accent-green: #57a746;
    --tag-blue: #1b6fb5;
    --ink-dark: #10222c;
    --badge-navy: #1559a8;
  }
  html, body {
    margin: 0;
    padding: 0;
    width: 1200px;
    height: 927px;
    overflow: hidden;
    background: var(--backdrop);
    font-family: "Montserrat", sans-serif;
  }
  .flyer {
    position: absolute;
    left: 260px;
    top: 23px;
    width: 680px;
    height: 880px;
    background: var(--paper);
    overflow: hidden;
    box-shadow: 0 6px 24px rgba(0,0,0,0.25);
  }
  .flyer-art {
    position: absolute;
    inset: 0;
  }
  .brand {
    position: absolute;
    right: 18px;
    top: 26px;
    display: flex;
    flex-direction: column;
    align-items: center;
    gap: 10px;
  }
  .brand-square {
    width: 44px;
    height: 44px;
    background: var(--brand-blue);
  }
  .brand-name {
    color: var(--brand-blue);
    font-weight: 700;
    font-size: 18px;
    letter-spacing: 0.5px;
  }
  .headline {
    position: absolute;
    left: 70px;
    top: 428px;
    color: #fff;
    margin: 0;
    line-height: 1;
  }
  .headline-kicker {
    display: block;
    font-weight: 500;
    font-size: 37px;
    letter-spacing: 0.5px;
  }
  .headline-main {
    display: block;
    margin-top: 8px;
    font-size: 47px;
    font-weight: 500;
  }
  .headline-main strong { font-weight: 800; }
  .rule {
    position: absolute;
    left: 69px;
    width: 517px;
    height: 1px;
    background: #fff;
  }
  .rule-top { top: 532px; }
  .intro {
    position: absolute;
    left: 71px;
    top: 545px;
    width: 500px;
    color: #fff;
    font-size: 13.4px;
    line-height: 16px;
  }
  .intro p { margin: 0 0 16px; }
  .tagline {
    position: absolute;
    left: 69px;
    top: 684px;
    width: 413px;
    height: 33px;
  }
  .tagline-shape { position: absolute; inset: 0; }
  .tagline-text {
    position: absolute;
    left: 19px;
    top: 0;
    line-height: 33px;
    color: var(--tag-blue);
    font-style: italic;
    font-weight: 600;
    font-size: 13.4px;
    white-space: nowrap;
  }
  .tagline-rule {
    position: absolute;
    left: 482px;
    top: 684px;
    width: 104px;
    height: 1px;
    background: #fff;
  }
  .insurance {
    position: absolute;
    left: 102px;
    top: 756px;
    width: 150px;
    height: 62px;
  }
  .insurance-pill {
    position: absolute;
    left: 40px;
    top: 12px;
    width: 109px;
    height: 36px;
    border-radius: 18px;
    background: var(--badge-navy);
  }
  .insurance-text {
    position: absolute;
    left: 60px;
    top: 16px;
    color: #fff;
    font-size: 11px;
    line-height: 13px;
  }
  .insurance-shield { position: absolute; left: 0; top: 0; }
  .call-prompt {
    position: absolute;
    right: 73px;
    top: 776px;
    color: var(--ink-dark);
    font-size: 12.4px;
  }
  .phone {
    position: absolute;
    left: 364px;
    top: 815px;
    display: flex;
    align-items: center;
    gap: 10px;
    color: #fff;
    font-weight: 700;
    font-size: 36px;
    line-height: 42px;
  }
</style>
</head>
<body>
  <div class="flyer">
    <svg class="flyer-art" width="680" height="880" viewBox="0 0 680 880" xmlns="http://www.w3.org/2000/svg">
      <defs>
        <linearGradient id="bodyGradient" x1="0" y1="0" x2="0" y2="1">
          <stop offset="0" stop-color="var(--band-blue)"/>
          <stop offset="0.2" stop-color="#2c84b0"/>
          <stop offset="1" stop-color="var(--band-green)"/>
        </linearGradient>
        <linearGradient id="photoGradient" x1="0" y1="0" x2="1" y2="0">
          <stop offset="0" stop-color="#8c98a4"/>
          <stop offset="0.35" stop-color="#c9d2d8"/>
          <stop offset="0.6" stop-color="#a9c7b0"/>
          <stop offset="0.8" stop-color="#58a74a"/>
          <stop offset="1" stop-color="#56a447"/>
        </linearGradient>
      </defs>
      <path class="photo-area" role="img" aria-label="Photo: smiling doctor in a white coat consulting with a patient, with a green DNA helix motif"
            d="M2,86 Q320,74 680,172 L680,408 Q340,352 2,378 Z" fill="url(#photoGradient)"/>
      <path class="body-band" d="M0,380 Q340,362 680,424 L680,880 L0,880 Z" fill="url(#bodyGradient)"/>
      <path class="footer-green" d="M0,852 L141,852 L114,880 L0,880 Z" fill="var(--accent-green)"/>
      <path class="footer-line" d="M0,849.5 L277,849.5 L314,813 Q322,805 334,805 L680,805" fill="none" stroke="#fff" stroke-width="3"/>
      <path class="footer-blue" d="M141,852 L278,852 L316,815 Q323,808 336,808 L680,808 L680,880 L114,880 Z" fill="var(--phone-blue)"/>
    </svg>

    <div class="brand">
      <div class="brand-square"></div>
      <div class="brand-name">Velmora Care</div>
    </div>

    <h1 class="headline">
      <span class="headline-kicker">IN-CENTER</span>
      <span class="headline-main"><strong>HEMODIALYSIS</strong> Clinic</span>
    </h1>
    <div class="rule rule-top"></div>

    <div class="intro">
      <p>We offer In-center hemodialysis for renal patients who prefer to have their treatments at a dialysis center.</p>
      <p>Our dialysis center has 6 Aqualine dialysis machines, supported by our state of the art water purification system. Pick up and drop off of patients is an additional service we offer for all in-center hemodialysis patients.</p>
    </div>

    <div class="tagline">
      <svg class="tagline-shape" width="413" height="33" viewBox="0 0 413 33" xmlns="http://www.w3.org/2000/svg">
        <path d="M0,0 L413,0 L388,24 Q378,33 362,33 L10,33 Q0,33 0,23 Z" fill="#fff"/>
      </svg>
      <span class="tagline-text">Transforming Lives, One Dialysis Session at a Time</span>
    </div>
    <div class="tagline-rule"></div>

    <div class="insurance">
      <div class="insurance-pill"></div>
      <svg class="insurance-shield" width="54" height="62" viewBox="0 0 54 62" xmlns="http://www.w3.org/2000/svg">
        <path d="M27,2 L51,12 L51,30 Q51,50 27,60 Q3,50 3,30 L3,12 Z" fill="var(--badge-navy)" stroke="#1d6fb8" stroke-width="2"/>
        <path d="M27,8 L45,16 L45,30 Q45,46 27,54 Q9,46 9,30 L9,16 Z" fill="none" stroke="var(--accent-green)" stroke-width="2"/>
        <path d="M17,31 L25,38 L38,23" fill="none" stroke="var(--accent-green)" stroke-width="4" stroke-linecap="round" stroke-linejoin="round"/>
      </svg>
      <div class="insurance-text">we accept<br>all insurances</div>
    </div>

    <div class="call-prompt">Call us now for more information!</div>

    <div class="phone">
      <svg width="26" height="26" viewBox="0 0 26 26" xmlns="http://www.w3.org/2000/svg" aria-hidden="true">
        <circle cx="13" cy="13" r="12" fill="#fff"/>
        <path d="M9,6 L11.5,9.5 L10,11.5 Q11.5,14.5 14.5,16 L16.5,14.5 L20,17 L18.5,19.5 Q12,20 8,14 Q5.5,9.5 7,7.5 Z" fill="var(--phone-blue)"/>
      </svg>
      <span>555-014-2870</span>
    </div>
  </div>
</body>
</html>
```